DESSERT FLYER

We need a flyer design for desserts and drinks for our restaurant.

We use Retro/rustic as main theme

Flyer must include all images, which are attached to this project. We also named correctly for each images, so you can use for each dish's title (docx file)
Must include our logo as well.

Flyer tittle is "DESSERT GLAZZ"

Please see our website for reference at copperlantern.com.au

Flyer's printing size is A5 Vertical. Single Side

```html
<!DOCTYPE html>
<html lang="en">
<head>
<meta charset="utf-8">
<title>Dessert Glazz – Copper Lantern</title>
<link rel="stylesheet" href="https://fonts.googleapis.com/css2?family=Alfa+Slab+One&family=Arvo:ital,wght@0,400;0,700;1,400;1,700&display=swap">
<style>
  :root {
    --wood-dark: #3a2414;
    --plank-line: #4a2a12;
    --paper: #f1f1ef;
    --paper-shade: #d9d9d6;
    --banner-dark: #232221;
    --banner-blue: #1d4a67;
    --title-orange: #d9743f;
    --title-teal: #1f8a96;
    --price-yellow: #f3d41c;
    --white: #ffffff;
    --ink: #3a2414;
  }
  * { margin: 0; padding: 0; box-sizing: border-box; }
  html, body { width: 846px; height: 1200px; overflow: hidden; background: var(--wood-dark); }
  .flyer { position: relative; width: 846px; height: 1200px; overflow: hidden; font-family: "Arvo", serif; }
  .backdrop { position: absolute; inset: 0; }
  .title {
    position: absolute; left: 78px; top: 42px;
    font-family: "Alfa Slab One", serif; font-size: 66px; letter-spacing: 2px; line-height: 1;
    color: var(--title-teal); font-weight: 400;
  }
  .title .accent { color: var(--title-orange); }
  .menu-item { position: absolute; left: 235px; width: 360px; text-align: center; color: var(--white); }
  .menu-item.blue { left: 255px; }
  .dish { font-size: 16px; letter-spacing: 4.5px; line-height: 20px; }
  .with { font-style: italic; font-size: 12px; line-height: 13px; }
  .extra { font-size: 16px; line-height: 20px; }
  .extra.small { font-size: 11.5px; }
  .extra.script { font-style: italic; font-size: 19px; line-height: 24px; }
  .price { font-style: italic; color: var(--price-yellow); font-size: 19px; line-height: 24px; margin-top: 8px; }
  .brand {
    position: absolute; left: 560px; top: 1100px; width: 250px; text-align: center;
    font-family: "Arvo", serif; font-weight: 400; font-size: 24px; letter-spacing: 3px;
    line-height: 1.2; color: var(--ink);
  }
</style>
</head>
<body>
<div class="flyer">
  <svg class="backdrop" width="846" height="1200" viewBox="0 0 846 1200">
    <defs>
      <linearGradient id="wood" x1="0" y1="0" x2="1" y2="0.3">
        <stop offset="0" stop-color="#7d4520"/>
        <stop offset="0.5" stop-color="#a8652e"/>
        <stop offset="1" stop-color="#8a4a20"/>
      </linearGradient>
      <radialGradient id="photo" cx="0.5" cy="0.5" r="0.6">
        <stop offset="0" stop-color="#e7c48a"/>
        <stop offset="1" stop-color="#6d7d3a"/>
      </radialGradient>
    </defs>

    <polygon points="0,250 846,150 846,1010 0,1110" fill="url(#wood)"/>
    <g stroke="var(--plank-line)" stroke-width="3" opacity="0.7">
      <line x1="0" y1="330" x2="846" y2="230"/>
      <line x1="0" y1="420" x2="846" y2="320"/>
      <line x1="0" y1="510" x2="846" y2="410"/>
      <line x1="0" y1="600" x2="846" y2="500"/>
      <line x1="0" y1="690" x2="846" y2="590"/>
      <line x1="0" y1="780" x2="846" y2="680"/>
      <line x1="0" y1="870" x2="846" y2="770"/>
      <line x1="0" y1="960" x2="846" y2="860"/>
      <line x1="0" y1="1050" x2="846" y2="950"/>
    </g>

    <polygon fill="var(--paper)" points="0,0 846,0 846,150 820,190 790,175 770,215 745,200 700,150 640,185 560,170 480,190 420,175 360,192 300,180 240,215 180,200 120,230 70,240 30,275 0,265"/>
    <polygon fill="var(--paper)" points="440,1200 455,1130 470,1090 520,1060 560,1000 610,990 660,975 700,955 760,962 800,945 846,950 846,1200"/>

    <line x1="275" y1="284" x2="830" y2="210" stroke="var(--white)" stroke-width="18" stroke-linecap="round" stroke-dasharray="0 35"/>
    <line x1="25" y1="1032" x2="580" y2="958" stroke="var(--white)" stroke-width="18" stroke-linecap="round" stroke-dasharray="0 35"/>

    <polygon fill="var(--banner-dark)" points="248,340 548,298 592,346 570,398 262,428 282,384"/>
    <polygon fill="var(--banner-blue)" points="290,433 600,400 612,490 275,520 250,483"/>
    <polygon fill="var(--banner-dark)" points="248,547 548,505 592,553 570,605 262,635 282,591"/>
    <polygon fill="var(--banner-blue)" points="290,638 600,605 612,710 275,740 250,698"/>
    <polygon fill="var(--banner-dark)" points="248,754 548,712 592,760 570,812 262,842 282,798"/>
    <polygon fill="var(--banner-blue)" points="290,846 600,813 612,918 275,948 250,906"/>

    <g stroke="var(--white)" stroke-width="4" stroke-linecap="round" stroke-dasharray="0 8" fill="none">
      <circle cx="150" cy="385" r="103"/>
      <circle cx="150" cy="612" r="103"/>
      <circle cx="150" cy="830" r="103"/>
      <circle cx="700" cy="405" r="103"/>
      <circle cx="700" cy="640" r="103"/>
      <circle cx="700" cy="855" r="103"/>
    </g>
    <circle cx="150" cy="385" r="95" fill="url(#photo)" role="img" aria-label="Photo: banana fritters on a banana leaf"/>
    <circle cx="150" cy="612" r="95" fill="#8a5a7a" role="img" aria-label="Photo: black sticky rice with mango cubes"/>
    <circle cx="150" cy="830" r="95" fill="#7a5a3e" role="img" aria-label="Photo: Vietnamese drip coffee being poured"/>
    <circle cx="700" cy="405" r="95" fill="#c9d8b8" role="img" aria-label="Photo: banana sago pudding on a leaf"/>
    <circle cx="700" cy="640" r="95" fill="#c98a3c" role="img" aria-label="Photo: fried ice cream with caramel topping"/>
    <circle cx="700" cy="855" r="95" fill="#c7a782" role="img" aria-label="Photo: fresh young coconut with straw"/>
  </svg>

  <h1 class="title"><span class="accent">DES</span>SERT GLAZZ</h1>

  <div class="menu-item" style="top:314px">
    <div class="dish">BANANA FRITTER</div>
    <div class="with">with</div>
    <div class="extra">VANILLA ICE CREAM</div>
    <div class="price">$6.90</div>
  </div>
  <div class="menu-item blue" style="top:414px">
    <div class="dish">BANANA SAGO PUDDING</div>
    <div class="with">with</div>
    <div class="extra">PEANUT TOPPING</div>
    <div class="price">$6.90</div>
  </div>
  <div class="menu-item" style="top:522px">
    <div class="dish">BLACK STICKY RICE</div>
    <div class="with">with</div>
    <div class="extra">MANGO</div>
    <div class="price">$6.90</div>
  </div>
  <div class="menu-item blue" style="top:622px">
    <div class="dish">FRIED ICE-CREAM</div>
    <div class="with">with</div>
    <div class="extra small">CARAMEL/CHOCOLATE/STRAWBERRY TOPPING</div>
    <div class="price">$6.90</div>
  </div>
  <div class="menu-item" style="top:732px">
    <div class="dish">VIETNAMESE</div>
    <div class="extra script">Coffee</div>
    <div class="price">$6.90</div>
  </div>
  <div class="menu-item blue" style="top:830px">
    <div class="dish">FRESH YOUNG</div>
    <div class="extra script">Coconut Juice</div>
    <div class="price">$5.50</div>
  </div>

  <div class="brand">COPPER LANTERN</div>
</div>
</body>
</html>
```